依頼詳細
チラシを持参してもらったお客様限定のお試し価格の案内チラシを作成したいと思います。
普段のお客様ですと、お店の高級感から敷居が高いように感じられがちですが、
今回は、少しライトな層を狙えるようなイメージを持っています。
記載項目
◆焼肉バー ミヨコ

・ぐるめ帳ページ
https://gurumecho.example/aichi/B4812/B481207/58194630/

・Picstream
https://www.picstream.example/miyoko_yakiniku_bar/
サイズ
A5
ページ数
片面
希望イメージ
シンプル 複雑
単色 カラフル
暗い 明るい
日常 高級
遊び心 厳粛
未来的 伝統的
女性的 男性的
希望する色
黄・オレンジ系、無彩色系
納品ファイル
• 高解像度JPG (.jpg)
• イラストレーター形式 (.ai)
補足説明

```html
<!DOCTYPE html>
<html lang="ja">
<head>
<meta charset="utf-8">
<title>焼肉バー ミヨコ お試しコース</title>
<link href="https://fonts.googleapis.com/css2?family=Noto+Sans+JP:wght@400;500;700;900&family=Noto+Serif+JP:wght@500;700;900&family=Oswald:wght@600;700&display=swap" rel="stylesheet">
<style>
:root{
  --ink:#111;
  --dark:#1c1a19;
  --orange:#f08a12;
  --orange-deep:#e25a0c;
  --red:#d8261a;
  --cream:#f6efe2;
  --white:#fff;
  --muted:#8a8580;
}
*{margin:0;padding:0;box-sizing:border-box}
html,body{width:844px;height:1200px;overflow:hidden;background:var(--ink)}
body{font-family:"Noto Sans JP",sans-serif;color:var(--white)}
.flyer{position:relative;width:844px;height:1200px;overflow:hidden;background:var(--ink)}

.hero-photo{position:absolute;left:0;top:0;width:844px;height:760px;
  background:radial-gradient(ellipse at 30% 22%,#b0343a 0%,#7a1e22 28%,#3a1412 52%,#141010 78%);}
.brand-box{position:absolute;right:22px;top:16px;width:92px;height:66px;background:rgba(0,0,0,.75);
  display:flex;flex-direction:column;align-items:center;justify-content:center;gap:6px}
.brand-box .dot{width:14px;height:14px;border:2px solid var(--white)}
.brand-box span{font-size:14px;font-weight:700;letter-spacing:.1em}
.tagline{position:absolute;left:540px;top:0;width:150px;height:330px;background:var(--cream);
  color:var(--ink);font-family:"Noto Serif JP",serif;font-weight:700;font-size:30px;line-height:1.45;
  writing-mode:vertical-rl;padding:22px 20px;letter-spacing:.08em}

.badge{position:absolute;left:14px;top:440px;width:270px;height:270px;border-radius:50%;
  background:var(--orange);color:var(--white);text-align:center;display:flex;flex-direction:column;
  justify-content:center;align-items:center;font-weight:900;font-size:27px;line-height:1.4;transform:rotate(-8deg)}
.badge .em{color:var(--ink);background:var(--white);padding:0 6px;margin:2px 0}
.badge .special{font-family:"Noto Serif JP",serif;font-style:italic;font-size:18px;font-weight:500;margin-top:6px}

.course{position:absolute;left:395px;top:498px;font-size:54px;font-weight:900;letter-spacing:.04em;line-height:1.3}
.price{position:absolute;left:285px;top:568px;font-family:"Oswald",sans-serif;font-weight:700;font-style:italic;
  font-size:160px;line-height:1;color:var(--orange);letter-spacing:-2px}
.price .yen{font-family:"Noto Sans JP",sans-serif;font-size:96px;font-weight:900;font-style:normal}
.tax{position:absolute;right:22px;top:585px;font-size:36px;font-weight:900}
.note{position:absolute;right:26px;top:736px;font-size:10px;color:#ccc}

.info{position:absolute;left:0;top:752px;width:844px;height:256px;background:var(--white);color:var(--ink)}
.info-tab{position:absolute;left:0;top:0;background:var(--dark);color:var(--white);font-family:"Oswald",sans-serif;
  font-size:24px;letter-spacing:.12em;padding:4px 28px 4px 22px}
.headline{position:absolute;left:22px;top:52px;display:flex;align-items:center;gap:14px}
.headline .new{font-family:"Noto Serif JP",serif;font-size:62px;font-weight:900;color:var(--orange-deep)}
.headline .genre{background:var(--red);color:var(--white);font-size:40px;font-weight:900;padding:4px 16px}
.lead{position:absolute;left:24px;top:150px;width:530px;font-size:16.5px;line-height:1.75;font-weight:500}
.menu{position:absolute;left:580px;top:14px;width:244px;height:232px;background:var(--dark);color:var(--white);
  padding:10px 20px;font-family:"Noto Serif JP",serif;font-size:15px;line-height:1.45;text-align:center}
.menu h3{font-style:italic;font-weight:500;font-size:18px;color:var(--orange);margin-bottom:2px;line-height:1.4}
.menu ul{list-style:none}

.call{position:absolute;left:0;top:1008px;width:844px;height:30px;background:var(--orange);color:var(--ink);
  font-size:17px;font-weight:700;padding-left:24px;line-height:30px}

.footer{position:absolute;left:0;top:1038px;width:844px;height:162px;background:var(--dark)}
.footer-brand{position:absolute;left:20px;top:22px;width:120px;height:120px;display:flex;flex-direction:column;
  align-items:center;justify-content:center;gap:8px}
.footer-brand .dot{width:18px;height:18px;border:2px solid var(--white)}
.footer-brand .name{font-size:18px;font-weight:700;letter-spacing:.1em}
.footer-brand .sub{font-size:9px;color:#bbb}
.notice{position:absolute;left:160px;top:12px;width:480px;border:2px solid var(--red);background:var(--white);
  color:var(--ink);font-size:13.5px;padding:4px 10px;line-height:1.45;font-weight:500}
.notice .hl{color:var(--red);font-weight:700}
.phone{position:absolute;left:160px;top:86px;display:flex;align-items:center;gap:10px}
.phone svg{width:44px;height:44px}
.phone .num{font-family:"Oswald",sans-serif;font-size:48px;font-weight:700;line-height:1}
.address{position:absolute;left:160px;top:140px;font-size:13px;display:flex;align-items:center;gap:6px}
.qr{position:absolute;left:690px;top:14px;width:130px;height:120px;background:var(--white)}
.qr-label{position:absolute;left:690px;top:138px;width:130px;font-size:11px;text-align:center;background:#333;color:var(--white)}
</style>
</head>
<body>
<main class="flyer">
  <div class="hero-photo" role="img" aria-label="網の上で焼かれる霜降りの和牛ステーキの写真"></div>
  <div class="brand-box"><i class="dot"></i><span>MIYOKO</span></div>
  <p class="tagline">上質なお肉を<br>リーズナブルに<br>ご提供します</p>

  <div class="badge">
    <span>このチラシを</span>
    <span>ご持参いただいた</span>
    <span class="em">お客様限定の</span>
    <span>お試し価格!!</span>
    <span class="special">Special Price</span>
  </div>

  <h1 class="course">お試しコース</h1>
  <p class="tax">(税込)</p>
  <p class="price">980<span class="yen">円</span></p>
  <p class="note">※写真はイメージです</p>

  <section class="info">
    <div class="info-tab">INFORMATION</div>
    <div class="headline"><span class="new">新感覚!</span><span class="genre">焼肉×バー</span></div>
    <p class="lead">洗練されたBARテイストの店内で厳選されたお肉をお楽しみください。無煙ロースターで衣服に匂いがつかないので出勤前や食事後でも安心してご利用いただけます。</p>
    <div class="menu">
      <h3>Menu</h3>
      <ul>
        <li>厚切り上タン</li>
        <li>黒毛和牛カルビ</li>
        <li>ミヨコサラダ</li>
        <li>本日の赤身</li>
        <li>特選タレハラミ</li>
        <li>テールの土瓶蒸し</li>
        <li>和牛ホルモン</li>
        <li>ライス</li>
      </ul>
    </div>
  </section>

  <div class="call">御予約、お問い合わせはお気軽にお電話ください</div>

  <footer class="footer">
    <div class="footer-brand"><i class="dot"></i><span class="name">ミヨコ</span><span class="sub">焼肉で新しい刺激を</span></div>
    <p class="notice"><span class="hl">チラシをご持参いただいたお客様のみの限定コース</span>です。ご来店の際、お持ちいただきスタッフにご提示ください。<br>※お試しコースの為、少量でのご提供となります。</p>
    <div class="phone">
      <svg viewBox="0 0 24 24" aria-hidden="true"><circle cx="12" cy="12" r="12" fill="#fff"/><path d="M8.2 6.5l1.8-.4 1.2 2.8-1.3 1a7 7 0 0 0 4.2 4.2l1-1.3 2.8 1.2-.4 1.8c-4.8.4-9.7-4.5-9.3-9.3z" fill="#1c1a19"/></svg>
      <span class="num">052-000-4187</span>
    </div>
    <p class="address">
      <svg width="12" height="16" viewBox="0 0 12 16" aria-hidden="true"><path d="M6 0a6 6 0 0 1 6 6c0 4-6 10-6 10S0 10 0 6a6 6 0 0 1 6-6z" fill="#f08a12"/><circle cx="6" cy="6" r="2.2" fill="#1c1a19"/></svg>
      愛知県名古屋市中区栄9-8-76 楓ビル2F
    </p>
    <div class="qr" role="img" aria-label="店舗ページへのコード"></div>
    <p class="qr-label">焼肉BAR ミヨコ</p>
  </footer>
</main>
</body>
</html>
```